Maple Hollow Grain Farm

We need a business card with some pizam in it. Our slogan is something different so something a little different would do!

Industry/Entity Type

Business

```html
<!DOCTYPE html>
<html lang="en">
<head>
<meta charset="utf-8">
<title>Maple Hollow Grain Farm – Business Card</title>
<link href="https://fonts.googleapis.com/css2?family=Alfa+Slab+One&family=Ubuntu:wght@400;500&display=swap" rel="stylesheet">
<style>
  :root {
    --page-bg: #ece8dc;
    --card-bg: #faf7e8;
    --olive: #6a7834;
    --olive-dark: #4e5a26;
    --olive-light: #8d9a55;
    --ink: #5b6630;
    --shadow: rgba(60, 50, 30, 0.18);
  }
  * { box-sizing: border-box; margin: 0; padding: 0; }
  html, body { width: 1200px; height: 900px; overflow: hidden; }
  body { background: var(--page-bg); position: relative; font-family: "Ubuntu", sans-serif; }

  .card {
    position: absolute;
    width: 560px;
    height: 320px;
    background: var(--card-bg);
    box-shadow: 0 6px 18px var(--shadow);
    overflow: hidden;
  }
  .card--front { left: 70px; top: 90px; }
  .card--back { left: 570px; top: 490px; }

  /* Front */
  .edge-band { position: absolute; width: 26px; background: var(--olive); }
  .edge-band--right { right: 0; top: 0; height: 62%; }
  .edge-band--left { left: 0; bottom: 0; height: 62%; }

  .front-brand {
    position: absolute;
    left: 0; right: 0; top: 70px;
    display: flex; flex-direction: column; align-items: center; gap: 12px;
  }
  .brand-mark { width: 46px; height: 46px; border-radius: 50%; background: var(--olive); }
  .brand-name {
    font-family: "Alfa Slab One", serif;
    color: var(--olive);
    font-size: 34px;
    letter-spacing: 1px;
    text-transform: uppercase;
    text-align: center;
    line-height: 1.1;
  }
  .slogan {
    position: absolute;
    left: 0; right: 0; bottom: 58px;
    text-align: center;
    font-family: "Alfa Slab One", serif;
    color: var(--olive-dark);
    font-size: 26px;
    letter-spacing: 1px;
    text-transform: uppercase;
  }

  /* Back */
  .contact-block { position: absolute; left: 40px; top: 92px; }
  .person-name {
    font-size: 25px; font-weight: 500; color: var(--ink);
    letter-spacing: 1px; text-transform: uppercase; margin-bottom: 12px;
  }
  .contact-list { list-style: none; }
  .contact-list li {
    display: flex; align-items: center; gap: 10px;
    font-size: 14px; font-weight: 500; color: var(--ink);
    margin-bottom: 8px;
  }
  .contact-icon { width: 12px; height: 12px; flex: none; fill: var(--ink); }
  .web-dot { width: 9px; height: 9px; border-radius: 50%; background: var(--ink); margin: 0 1.5px; flex: none; }

  .state-area {
    position: absolute; right: 30px; top: 26px;
    width: 230px; height: 150px;
    background: linear-gradient(160deg, var(--olive-light), var(--olive));
    border-radius: 14px 40px 10px 60px;
  }
  .address {
    position: absolute; right: 30px; top: 188px;
    display: flex; align-items: center; gap: 6px;
    font-size: 12px; color: var(--ink);
  }
  .address svg { width: 10px; height: 14px; fill: var(--ink); }

  .back-brand {
    position: absolute; left: 150px; bottom: 34px;
    display: flex; align-items: center; gap: 8px;
  }
  .back-brand .brand-mark { width: 20px; height: 20px; }
  .back-brand .brand-label {
    font-size: 15px; font-weight: 500; color: var(--olive); text-transform: uppercase; letter-spacing: 0.5px;
  }
</style>
</head>
<body>

  <section class="card card--front" aria-label="Business card front">
    <div class="edge-band edge-band--right"></div>
    <div class="edge-band edge-band--left"></div>
    <div class="front-brand">
      <span class="brand-mark"></span>
      <h1 class="brand-name">Maple Hollow<br>Grain Farm</h1>
    </div>
    <p class="slogan">Something Different</p>
  </section>

  <section class="card card--back" aria-label="Business card back">
    <div class="contact-block">
      <h2 class="person-name">Daniel Marsh</h2>
      <ul class="contact-list">
        <li>
          <svg class="contact-icon" viewBox="0 0 24 24" aria-hidden="true"><path d="M6.6 10.8a15.1 15.1 0 0 0 6.6 6.6l2.2-2.2a1 1 0 0 1 1-.25 11.4 11.4 0 0 0 3.6.57 1 1 0 0 1 1 1V20a1 1 0 0 1-1 1A17 17 0 0 1 3 4a1 1 0 0 1 1-1h3.5a1 1 0 0 1 1 1c0 1.25.2 2.45.57 3.57a1 1 0 0 1-.25 1z"/></svg>
          5550142786
        </li>
        <li>
          <svg class="contact-icon" viewBox="0 0 24 24" aria-hidden="true"><path d="M2 5h20v14H2z M3 6l9 7 9-7" stroke="#faf7e8" stroke-width="1.5"/></svg>
          dmarsh@example.com
        </li>
        <li>
          <span class="web-dot"></span>
          www.example.com/maplehollowgrain
        </li>
      </ul>
    </div>

    <div class="state-area" role="img" aria-label="Silhouette map of New York State"></div>
    <p class="address">
      <svg viewBox="0 0 10 14" aria-hidden="true"><path d="M5 0a5 5 0 0 1 5 5c0 3.5-5 9-5 9S0 8.5 0 5a5 5 0 0 1 5-5zm0 3a2 2 0 1 0 0 4 2 2 0 0 0 0-4z"/></svg>
      120 Orchard Lane, Fairview, NY 10000
    </p>

    <div class="back-brand">
      <span class="brand-mark"></span>
      <span class="brand-label">Maple Hollow Grain Farm</span>
    </div>
  </section>

</body>
</html>
```